"Sail Past Amber Dunes" Book Cover Design

I am seeking a dynamic, modern, and professional cover design for a book focused on groundbreaking science that explores how a supplement called plasmalogens can revitalize the brain, prevent Alzheimer’s, and safeguard memories. The design should strike a balance between being visually appealing and conveying the seriousness of the topic.

Target Market(s)

The target audience includes individuals who are curious about cutting-edge science and proactive approaches to brain health, as well as those seeking to better understand how to protect their cognitive functions and memories. The cover should resonate with readers interested in health, science, and self-improvement, while reflecting the book’s informative and empowering tone.

Requirements
Must have
• The quotation across the top of the page (this is a placeholder for now, it will be changed eventually) and the author's name.
Should not have
• You don't need to use the puzzle idea!

```html
<!DOCTYPE html>
<html lang="en">
<head>
<meta charset="utf-8">
<title>How to Sail Past Amber Dunes — Cover</title>
<link rel="stylesheet" href="https://fonts.googleapis.com/css2?family=Montserrat:wght@700;800;900&family=Tinos:ital@1&display=swap">
<style>
  :root {
    --ink: #0b1622;
    --white: #ffffff;
    --mist: #e6eff3;
    --sky: #bcd3dd;
    --slate: #7f9fb0;
    --deep: #3f5d6e;
    --art-dark: #1e3344;
    --art-red: #9b3a45;
  }
  * { margin: 0; padding: 0; box-sizing: border-box; }
  html, body { width: 1200px; height: 864px; overflow: hidden; }
  body { font-family: "Montserrat", Arial, sans-serif; }

  .cover {
    position: relative;
    width: 1200px;
    height: 864px;
    overflow: hidden;
    background:
      radial-gradient(ellipse 380px 300px at 180px 430px, rgba(255,255,255,0.95), rgba(255,255,255,0) 70%),
      radial-gradient(ellipse 700px 500px at 1200px 864px, rgba(63,93,110,0.75), rgba(63,93,110,0) 75%),
      linear-gradient(90deg, var(--mist) 0%, #d6e5ec 45%, var(--sky) 70%, var(--slate) 100%);
  }

  .cover-art {
    position: absolute;
    left: 380px;
    top: 290px;
    width: 560px;
    height: 574px;
    background:
      radial-gradient(ellipse 210px 300px at 340px 300px, rgba(30,51,68,0.9), rgba(30,51,68,0) 100%),
      radial-gradient(ellipse 160px 200px at 260px 260px, rgba(155,58,69,0.55), rgba(155,58,69,0) 100%),
      radial-gradient(ellipse 200px 240px at 130px 200px, rgba(214,170,160,0.5), rgba(214,170,160,0) 100%);
  }

  .spine {
    position: absolute;
    left: 577px;
    top: 0;
    width: 47px;
    height: 864px;
    background: rgba(255,255,255,0.28);
  }
  .spine-title, .spine-author {
    position: absolute;
    left: 50%;
    white-space: nowrap;
    font-weight: 800;
    transform-origin: center;
  }
  .spine-title {
    top: 325px;
    color: var(--ink);
    font-size: 19px;
    letter-spacing: 0.22em;
    transform: translate(-50%, -50%) rotate(-90deg);
  }
  .spine-author {
    top: 700px;
    color: var(--white);
    font-size: 11px;
    letter-spacing: 0.16em;
    transform: translate(-50%, -50%) rotate(-90deg);
  }

  .endorsement {
    position: absolute;
    left: 640px;
    width: 540px;
    top: 22px;
    text-align: center;
    font-family: "Tinos", "Times New Roman", serif;
    font-style: italic;
    font-size: 14.5px;
    line-height: 1.3;
    color: var(--ink);
  }

  .title {
    position: absolute;
    right: 63px;
    top: 72px;
    text-align: right;
    font-weight: 900;
    line-height: 1;
  }
  .title-lead {
    display: block;
    font-size: 33px;
    letter-spacing: 0.2em;
    color: var(--ink);
    margin-right: -0.2em;
  }
  .title-main {
    display: block;
    font-size: 91px;
    letter-spacing: 0.09em;
    margin-right: -0.09em;
    color: var(--ink);
    margin-top: 10px;
  }
  .title-last {
    display: block;
    font-size: 108px;
    letter-spacing: 0.16em;
    margin-right: -0.16em;
    color: var(--white);
    margin-top: 6px;
    text-shadow: 0 2px 4px rgba(0,0,0,0.15);
  }

  .subtitle {
    position: absolute;
    right: 63px;
    top: 392px;
    text-align: right;
    font-weight: 800;
    line-height: 1;
  }
  .subtitle span { display: block; }
  .sub-key {
    font-size: 31px;
    letter-spacing: 0.14em;
    margin-right: -0.14em;
  }
  .sub-line {
    font-size: 15px;
    letter-spacing: 0.16em;
    margin-right: -0.16em;
    color: var(--ink);
    margin: 8px 0 10px;
  }
  .sub-key.dark { color: var(--ink); }
  .sub-key.light { color: var(--white); }

  .author {
    position: absolute;
    right: 83px;
    top: 812px;
    font-weight: 800;
    font-size: 25px;
    letter-spacing: 0.18em;
    color: var(--white);
    white-space: nowrap;
  }
</style>
</head>
<body>
  <div class="cover">
    <div class="cover-art" role="img" aria-label="Profile of a human head dissolving into scattered puzzle pieces in dark blue, red and pale peach tones"></div>

    <div class="spine">
      <span class="spine-title">HOW TO SAIL PAST AMBER DUNES</span>
      <span class="spine-author">OWEN HARTLEY, MD</span>
    </div>

    <p class="endorsement">“An incredible guide to protecting your mind and memories."<br>-Leona Marsh, MD</p>

    <h1 class="title">
      <span class="title-lead">HOW TO SAIL PAST</span>
      <span class="title-main">AMBER</span>
      <span class="title-last">DUNES</span>
    </h1>

    <p class="subtitle">
      <span class="sub-key dark">RESTORE</span>
      <span class="sub-line">YOUR MEMORY,</span>
      <span class="sub-key light">PREVENT</span>
      <span class="sub-line">ALZHEIMER’S, AND</span>
      <span class="sub-key light">REVERSE</span>
      <span class="sub-line">THE AGE OF YOUR</span>
      <span class="sub-key dark">MIND</span>
    </p>

    <p class="author">OWEN HARTLEY, MD</p>
  </div>
</body>
</html>
```